A specialised Sport management needs a corporate brochure design

We are a specialized company in the management and consultancy of sports events. and need to have a company brochure
We provide the following services;
Event management
Venues management
Production
Ticketing
Consulting
Hospitality
Activity management
Event timing
Branding of event
Event supplies
We need a corporate profile design for our company to showcase the major events that we have covered , with images, information, statistics, surveys, products and services used. We want to highlight our professionalism and execution of the events, experience of the participants, spectators . How we have grown in the past few years and reached the international standards.
Objectives of the work:
To get sponsors and partners for future business and to present Keel-Marrow
as not just a sports management company but also a professional sports
events management company.
You can check our website
www.keel-marrow.example
Target Market(s)
Sponsors and corporate partners
Industry/Entity Type
Events
Font styles to use
Requirements
Must have
- Must Have:
- - Very professional look
- -Some event images,Event information, statistics, surveys, products and services used. We want to highlight our professionalism and execution of the events (Attached)
Nice to have
- Similar momentom of the below design
- http://www.dunlathgames.example/wp-content/themes/dunlath_games/pdf/CP-2014-15-V10-Web.pdf

```html
<!DOCTYPE html>
<html lang="en">
<head>
<meta charset="utf-8">
<title>Keel-Marrow Events Calendar Brochure</title>
<link rel="stylesheet" href="https://fonts.googleapis.com/css2?family=Cinzel:wght@700&family=EB+Garamond:ital,wght@0,400;0,600;1,400&display=swap">
<style>
:root{
  --orange:#ee5a24;
  --orange-soft:#f08a4b;
  --ink:#333;
  --grey:#8a8f94;
  --light:#e6e7e8;
  --white:#fff;
  --quote:#f3c338;
}
*{margin:0;padding:0;box-sizing:border-box}
html,body{width:1200px;height:431px;overflow:hidden;background:var(--white)}
body{font-family:"EB Garamond",Georgia,serif;color:var(--ink)}
.spread{position:relative;width:1200px;height:431px;overflow:hidden}

/* panel 1: cover photo */
.crowd-photo{position:absolute;left:0;top:0;width:300px;height:431px;
  background:linear-gradient(160deg,#8c9a86 0%,#5f6b5a 40%,#3e4a3c 70%,#2c3329 100%)}
.calendar-banner{position:absolute;left:0;top:0;width:215px;height:76px;background:var(--orange);
  clip-path:polygon(0 0,100% 0,96% 30%,100% 55%,95% 80%,98% 100%,0 100%)}
.calendar-banner h1{font-family:"Cinzel",Georgia,serif;font-weight:700;color:var(--white);
  font-size:17px;line-height:21px;text-align:center;padding:15px 10px 0 0}
.testimonial{position:absolute;left:30px;top:330px;width:170px;font-size:8px;line-height:10px}
.testimonial p{font-style:italic;color:var(--quote)}
.testimonial cite{display:block;margin-top:5px;font-style:normal;color:var(--white);font-size:7.5px;line-height:9px}

/* panel 2: calendar */
.calendar{position:absolute;left:300px;top:0;width:300px;height:431px}
.timeline{position:absolute;left:0;top:0}
.event{position:absolute;width:58px;text-align:center;font-size:6.5px;line-height:8px}
.event .mark{display:block;margin:0 auto 2px;width:44px;height:16px;border-radius:3px}
.event .name{display:block;font-weight:600;font-size:7px}
.contact{position:absolute;right:22px;top:331px;text-align:right;font-size:9px;line-height:11.5px}
.contact h2{font-size:10px;font-weight:600;margin-bottom:8px}
.social{margin-top:10px;display:flex;justify-content:flex-end;align-items:center;gap:4px}
.social .square{width:10px;height:10px;background:#4b9bd6}

/* panels 3–4: company */
.race-photo{position:absolute;left:600px;top:0;width:420px;height:431px;
  background:linear-gradient(150deg,#b9b1a8 0%,#8b8279 35%,#5b4f47 65%,#2d2b2c 100%);
  clip-path:polygon(0 0,150px 0,400px 431px,0 431px)}
.accent-band{position:absolute;inset:0}
.brand{position:absolute;left:862px;top:78px;display:flex;flex-direction:column;align-items:center;width:96px}
.brand .circle{width:46px;height:46px;border-radius:50%;background:var(--orange)}
.brand .name{margin-top:6px;font-size:14px;font-weight:600;color:var(--ink)}
.divider{position:absolute;left:966px;top:64px;width:1px;height:98px;background:var(--grey)}
.about{position:absolute;left:975px;top:62px;width:205px;font-size:10px;line-height:12.5px;color:#555}
</style>
</head>
<body>
<main class="spread">

  <section class="cover">
    <div class="crowd-photo" role="img" aria-label="Event host speaking into a microphone in front of a crowd"></div>
    <div class="calendar-banner"><h1>EVENTS CALENDAR<br>2015</h1></div>
    <blockquote class="testimonial">
      <p>"CONGRATULATIONS on a great event last weekend. The team was a pleasure to work with and every detail was handled with care. I was impressed by the standard of organisation, the timing and the warm welcome given to all riders and families on the day."</p>
      <cite>Conrad Ellery<br>G.M - Brightwater club</cite>
    </blockquote>
  </section>

  <section class="calendar">
    <svg class="timeline" width="300" height="300" viewBox="0 0 300 300">
      <g fill="none" stroke="var(--orange)" stroke-width="2.5">
        <path d="M32 78 H275 V123 H25 V168 H275"/>
      </g>
    </svg>

    <div class="event" style="left:10px;top:34px"><span class="mark" style="background:#e8732c"></span><span class="name">Harbor Run</span>7th to 10th Jan</div>
    <div class="event" style="left:83px;top:34px"><span class="mark" style="background:#c8282d"></span><span class="name">Ridgeline</span>7th Feb</div>
    <div class="event" style="left:156px;top:34px"><span class="mark" style="background:#7d3f98"></span><span class="name">Kestrel</span>3rd &amp; 4th Apr</div>
    <div class="event" style="left:228px;top:34px"><span class="mark" style="background:#5aa83c"></span><span class="name">Outer Edge</span>13-28 June</div>

    <div class="event" style="left:42px;top:84px"><span class="mark" style="background:#1d6fb8"></span><span class="name">Dune Trail</span>14th - 17th Jan</div>
    <div class="event" style="left:120px;top:84px"><span class="mark" style="background:#4a4a4a"></span><span class="name">Grit Race</span>13th &amp; 14th Mar (12 Hr Karting)</div>
    <div class="event" style="left:200px;top:84px"><span class="mark" style="background:#b8202a"></span><span class="name">Coastal Tri</span>16th Jun to 4th Jul</div>

    <div class="event" style="left:42px;top:130px"><span class="mark" style="background:#3c8f3a"></span><span class="name">Coastal Tri</span>31st Oct</div>
    <div class="event" style="left:120px;top:130px"><span class="mark" style="background:#d7262e"></span><span class="name">Ridgeline</span>14th Nov</div>
    <div class="event" style="left:200px;top:130px"><span class="mark" style="background:#f2b705"></span><span class="name">Ember</span>5th Dec</div>

    <div class="event" style="left:10px;top:176px"><span class="mark" style="background:#f2b705"></span><span class="name">Ember</span>24th Oct</div>
    <div class="event" style="left:83px;top:176px"><span class="mark" style="background:#d9b24a"></span><span class="name">Coastal Tri</span>7th Nov</div>
    <div class="event" style="left:156px;top:176px"><span class="mark" style="background:#c8102e"></span><span class="name">Kestrel</span>27th Nov</div>
    <div class="event" style="left:228px;top:176px"><span class="mark" style="background:#4a4a4a"></span><span class="name">Grit Race</span>10th to 12th Dec (24 Hr Karting)</div>

    <address class="contact">
      <h2>Contact Us</h2>
      Mob: 965 5550 1289<br>
      Tel: 965 5550 4417<br>
      Email: events@keel-marrow.example<br>
      Website: www.keel-marrow.example
      <div class="social"><span class="square"></span><span>KMsportevents</span></div>
    </address>
  </section>

  <section class="company">
    <div class="race-photo" role="img" aria-label="Kart drivers in helmets celebrating with flag-waving spectators"></div>
    <svg class="accent-band" width="1200" height="431" viewBox="0 0 1200 431">
      <polygon points="750,0 790,0 1040,431 1000,431" fill="var(--light)" opacity="0.7"/>
      <polygon points="1060,431 1200,340 1200,431" fill="var(--light)"/>
      <polygon points="1120,431 1200,378 1200,431" fill="var(--orange)"/>
      <polygon points="1165,431 1200,408 1200,431" fill="var(--grey)"/>
    </svg>
    <div class="brand"><span class="circle"></span><span class="name">Keel-Marrow</span></div>
    <div class="divider"></div>
    <p class="about">Keel-Marrow is the leading company in Kuwait, which specialises in the management and consultancy of sports events. Established in 2007, Keel-Marrow has grown in stature and strength over the years, to become the renowned establishment it is today in this highly specialised field.</p>
  </section>

</main>
</body>
</html>
```